Personal Training Business Card Design

I have just started my own personal training business called "Lana Corvell Fitness". My goal as a personal trainer is to motivate, inspire and educate all of my clients about the benefits of regular exercise, nourishing the body with nutritious foods and living healthy. I train both men and women, so I would like a business card that will appeal to both sexes and not come across too feminine or too masculine. I'm looking for a fresh, yet simple look which uses "fresh" colours such as green, white and grey - similar to my logo (but open to other effective gender-neutral colour schemes). I am open to using the logo I have uploaded as one image together, or separating the text and image (also supplied).
Industry/Entity Type
Personal Trainer
Contact Information for Business Card
Lana Corvell
Fitness Coach
Address: Ground Floor, Maplewick House, 342 Larkin St, Brisbane City, 4000
Email: lanacorvellfitness@mailorbit.net
Phone: 0455 293 604
SocialNook: www.socialnook.net/lanacorvellfitness
Look and feel

```html
<!DOCTYPE html>
<html lang="en">
<head>
<meta charset="utf-8">
<title>Lana Corvell Fitness – Business Card</title>
<link href="https://fonts.googleapis.com/css2?family=Montserrat:wght@400&family=Roboto+Condensed:wght@400;700&display=swap" rel="stylesheet">
<style>
  :root {
    --green: #8cc63f;
    --grey: #808080;
    --grey-dark: #6d6e71;
    --border: #d0d0d0;
    --paper: #ffffff;
  }
  * { margin: 0; padding: 0; box-sizing: border-box; }
  html, body { width: 957px; height: 1200px; overflow: hidden; background: var(--paper); }
  .canvas { position: relative; width: 957px; height: 1200px; }

  .card { position: absolute; left: 0; width: 957px; background: var(--paper); border: 1px solid var(--border); }
  .card--front { top: 0; height: 591px; }
  .card--back { top: 607px; height: 593px; }

  /* Front */
  .brand-mark {
    position: absolute; left: 361px; top: 126px;
    width: 238px; height: 238px; border-radius: 50%;
    background: var(--green);
  }
  .brand-name {
    position: absolute; left: 0; right: 0; top: 383px;
    text-align: center;
    font-family: "Montserrat", sans-serif; font-weight: 400;
    font-size: 36px; letter-spacing: 0.5px;
    color: var(--green);
  }
  .tagline {
    position: absolute; left: 0; right: 0; top: 436px;
    text-align: center;
    font-family: "Montserrat", sans-serif; font-weight: 400;
    font-size: 27px; color: var(--grey-dark);
  }
  .front-band {
    position: absolute; left: 0; right: 0; top: 552px; height: 37px;
    background: var(--green);
  }

  /* Back */
  .rule { position: absolute; left: 318px; width: 4px; background: var(--green); }
  .rule--top { top: 2px; height: 113px; }
  .rule--bottom { top: 478px; bottom: 0; }

  .person { position: absolute; left: 319px; top: 130px; font-family: "Roboto Condensed", sans-serif; }
  .person__name { font-weight: 700; font-size: 31px; line-height: 36px; color: var(--grey); }
  .person__first { color: var(--green); }
  .person__role { font-weight: 400; font-size: 23px; line-height: 30px; color: var(--grey-dark); }

  .contact-list { position: absolute; left: 319px; top: 0; list-style: none; font-family: "Roboto Condensed", sans-serif; }
  .contact-item { position: absolute; left: 0; white-space: nowrap; }
  .contact-icon {
    position: absolute; left: 0; top: 0; width: 36px; height: 36px;
    border-radius: 4px; background: var(--green);
  }
  .contact-icon svg { display: block; width: 36px; height: 36px; }
  .contact-text {
    position: absolute; left: 59px; top: 0;
    font-size: 23px; line-height: 32px; color: var(--grey-dark);
  }
  .contact-item--address { top: 252px; }
  .contact-item--email { top: 329px; }
  .contact-item--phone { top: 375px; }
  .contact-item--social { top: 422px; }
</style>
</head>
<body>
<div class="canvas">

  <section class="card card--front">
    <div class="brand-mark"></div>
    <div class="brand-name">LANA CORVELL FITNESS</div>
    <div class="tagline">motivate. inspire. educate.</div>
    <div class="front-band"></div>
  </section>

  <section class="card card--back">
    <div class="rule rule--top"></div>
    <div class="rule rule--bottom"></div>

    <div class="person">
      <div class="person__name"><span class="person__first">LANA</span> CORVELL</div>
      <div class="person__role">FITNESS COACH</div>
    </div>

    <ul class="contact-list">
      <li class="contact-item contact-item--address">
        <span class="contact-icon">
          <svg viewBox="0 0 36 36"><path d="M18 7a7.5 7.5 0 0 0-7.5 7.5C10.5 20 18 29 18 29s7.5-9 7.5-14.5A7.5 7.5 0 0 0 18 7z" fill="#fff"/><circle cx="18" cy="14.5" r="3" fill="#8cc63f"/></svg>
        </span>
        <span class="contact-text">Ground Floor, Maplewick House,<br>342 Larkin St, Brisbane City, 4000</span>
      </li>
      <li class="contact-item contact-item--email">
        <span class="contact-icon">
          <svg viewBox="0 0 36 36"><rect x="8" y="11" width="20" height="14" fill="none" stroke="#fff" stroke-width="2"/><path d="M8 11l10 8 10-8M8 25l7-7M28 25l-7-7" fill="none" stroke="#fff" stroke-width="1.6"/></svg>
        </span>
        <span class="contact-text">Email: lanacorvellfitness@mailorbit.net</span>
      </li>
      <li class="contact-item contact-item--phone">
        <span class="contact-icon">
          <svg viewBox="0 0 36 36"><rect x="12" y="6" width="12" height="24" rx="2" fill="none" stroke="#fff" stroke-width="2"/><rect x="14.5" y="10" width="7" height="6" fill="#fff"/><g fill="#fff"><rect x="14.5" y="18.5" width="2" height="2"/><rect x="17" y="18.5" width="2" height="2"/><rect x="19.5" y="18.5" width="2" height="2"/><rect x="14.5" y="21.5" width="2" height="2"/><rect x="17" y="21.5" width="2" height="2"/><rect x="19.5" y="21.5" width="2" height="2"/><rect x="14.5" y="24.5" width="2" height="2"/><rect x="17" y="24.5" width="2" height="2"/><rect x="19.5" y="24.5" width="2" height="2"/></g></svg>
        </span>
        <span class="contact-text">Phone: 0455 293 604</span>
      </li>
      <li class="contact-item contact-item--social">
        <span class="contact-icon">
          <svg viewBox="0 0 36 36"><g fill="none" stroke="#fff" stroke-width="1.6"><circle cx="18" cy="18" r="10"/><ellipse cx="18" cy="18" rx="4.5" ry="10"/><path d="M8 18h20M10 13h16M10 23h16"/></g></svg>
        </span>
        <span class="contact-text">SocialNook : www.socialnook.net/lanacorvellfitness</span>
      </li>
    </ul>
  </section>

</div>
</body>
</html>
```